Tree Pruning Website

We need a website for a tree Arborist, pruning company called Hollow Ridge Groundcare. We look after all types of trees, knock down trees and prune trees. Our target market is from domestic clients to government clients and everything in between.

We would like to see the use of our main colours which are orange and green

We are not looking forward in seeing a template that we have seen before but a unique template. We have designed 5 templates ourselves and we wish for the design community to take our designs to the next level.

We have also designed a template for things that **we are not** looking for (Version 4)

To make it fair for everyone, we are also not giving out any participation payments as we have had. One winner will take all of the payment!!!

I Have attached a image of the designs and a image of a tree.

We are just looking at the PSD file been developed. We have our own team who can slice the image up into a HTML format.

Target Market(s)

Everyone who needs to cut down a tree

Industry/Entity Type

Government

Requirements
Must have
• Logo on front page
A List of our services
jQuery slider on page
Phone Number on every page

```html
<!DOCTYPE html>
<html lang="en">
<head>
<meta charset="utf-8">
<title>Hollow Ridge Groundcare</title>
<link href="https://fonts.googleapis.com/css2?family=Arimo:ital,wght@0,400;0,700;1,400&display=swap" rel="stylesheet">
<style>
:root{
  --nav-top:#4a4a4a;--nav-bot:#262626;
  --hero-top:#5a7f48;--hero-bot:#3c5e2f;
  --page:#eef3f5;
  --green-title:#4d7a3b;
  --orange:#e8801e;--orange-top:#f6a54a;--orange-bot:#d46f12;
  --body-text:#6b6b6b;
  --pill:#d3dfe3;
  --foot-top:#4a4a4a;--foot-bot:#232323;
  --social:#7fb73a;
}
*{box-sizing:border-box;margin:0;padding:0}
html,body{width:952px;height:1200px;overflow:hidden}
body{font-family:"Arimo",Arial,sans-serif;background:var(--page);position:relative}
.abs{position:absolute}

/* nav */
.nav{position:absolute;top:0;left:0;width:952px;height:50px;background:linear-gradient(var(--nav-top),var(--nav-bot));border-bottom:1px solid #6a6a6a}
.nav ul{list-style:none;position:absolute;left:71px;top:0;height:50px;display:flex}
.nav li{height:50px;display:flex;align-items:center;justify-content:center;color:#cfcfcf;font-size:11.5px;border-right:1px solid #1c1c1c;box-shadow:1px 0 0 #555}
.nav li.active{background:#1f1f1f;color:#fff;border-bottom:3px solid var(--orange)}
.nav .call{position:absolute;left:688px;top:0;width:194px;height:50px;display:flex;align-items:center;justify-content:center;color:#fff;font-size:15px;border-right:1px solid #1c1c1c;border-left:1px solid #1c1c1c}
.nav .call b{color:var(--orange-top);font-weight:400;margin-left:5px}

/* hero */
.hero{position:absolute;top:51px;left:0;width:952px;height:360px;background:linear-gradient(var(--hero-top),var(--hero-bot))}
.logo{left:71px;top:30px;display:flex;align-items:center;gap:12px}
.logo-mark{width:40px;height:40px;border-radius:50%;background:var(--orange);flex:none}
.logo-name{color:#fff;font-size:26px;font-weight:700;line-height:28px}
.rule{left:71px;width:338px;height:2px;background:#2f4a25;border-bottom:1px solid #6f955c}
.welcome{left:72px;top:132px;color:#fff;font-size:20px;font-weight:400}
.intro{left:72px;top:163px;width:340px;color:#f0f3ec;font-size:10.6px;line-height:18.2px}
.quote-btn{left:72px;top:268px;width:180px;height:32px;border-radius:16px;background:linear-gradient(var(--orange-top),var(--orange-bot));box-shadow:0 2px 3px rgba(0,0,0,.35);display:flex;align-items:center;padding-left:20px;gap:11px;color:#fff;font-size:15px;font-weight:700;letter-spacing:.3px}
.slider{left:429px;top:28px;width:453px;height:302px;background:#fff;padding:4px;box-shadow:0 10px 12px -6px rgba(0,0,0,.45)}
.slider .ph{width:100%;height:100%;background:linear-gradient(160deg,#7e9a6a,#b9c8b4 45%,#e6e2d8 75%,#8c9fb4)}
.slider-arrows{left:637px;top:316px;display:flex;gap:2px}

/* features */
.feature{position:absolute;top:434px;width:242px}
.feature h2,.section-title{color:var(--green-title);font-weight:400;font-size:17px}
.feature .frame{margin-top:12px;height:116px;background:#fff;padding:4px;box-shadow:0 0 2px rgba(0,0,0,.15)}
.feature .ph{height:100%}
.feature p{margin-top:14px;color:var(--body-text);font-size:10.5px;line-height:18.2px;text-align:justify}
.btn-more{display:inline-block;margin-top:14px;height:23px;padding:0 9px;line-height:23px;background:linear-gradient(#6c6c6c,#4a4a4a);color:#eee;font-size:10.5px;border-radius:3px;box-shadow:0 2px 2px rgba(0,0,0,.3)}
.divider{left:71px;top:739px;width:811px;height:1px;background:#c9cfd1}

/* services list */
.services{left:82px;top:762px}
.services ul{list-style:none;margin-top:14px}
.services li{width:222px;height:27px;margin-bottom:3.6px;border-radius:14px;background:var(--pill);display:flex;align-items:center;gap:14px;padding-left:6px;color:#3e3e3e;font-size:12.5px}
.services li svg{flex:none}

/* about */
.about{left:354px;top:762px;width:520px}
.about p{margin-top:14px;width:388px;color:var(--body-text);font-size:10.5px;line-height:18.2px}
.about .mascot{position:absolute;left:408px;top:24px;width:103px;height:97px;border-radius:50% 50% 40% 40%;background:radial-gradient(circle at 40% 40%,#c9d6c2,#9aa9a6)}
.gallery{left:353px;top:905px;width:520px;height:132px;background:var(--pill);display:flex;gap:11px;padding:13px}
.gallery .frame{flex:1;background:#fff;padding:3px}
.gallery .ph{height:100%}

/* footer */
.footer{position:absolute;left:0;top:1056px;width:952px;height:144px;background:linear-gradient(var(--foot-top),var(--foot-bot))}
.footer h3{font-weight:400;color:#e8e8e8;font-size:13.5px;position:absolute}
.vline{position:absolute;top:16px;width:1px;height:118px;background:#555;box-shadow:1px 0 0 #2a2a2a}
.map{left:84px;top:41px;width:121px;height:86px;background:#fff;padding:3px}
.map .ph{height:100%;background:linear-gradient(135deg,#e6e3db,#d5d2c6)}
.contact{left:218px;top:40px;color:#ddd;font-size:10.5px;line-height:18.2px;font-style:normal}
.testimonial{left:394px;top:48px;width:196px;color:#ddd;font-style:italic;font-size:10.5px;line-height:16.6px;text-align:justify}
.quote-mark{font-size:18px;font-style:normal;color:var(--orange-top);line-height:0}
.customer{left:394px;top:107px;color:#eee;font-style:italic;font-size:11.5px}
.social{left:761px;top:16px;display:flex;gap:8px}
.social span{width:20px;height:20px;border-radius:50%;background:var(--social);box-shadow:inset 0 -2px 0 rgba(0,0,0,.2)}
.copy{right:89px;top:51px;color:#ddd;font-size:10.5px;text-align:right;line-height:27px}
</style>
</head>
<body>

<nav class="nav">
  <ul>
    <li class="active" style="width:77px">Home</li>
    <li style="width:104px">About us</li>
    <li style="width:119px">Our Services</li>
    <li style="width:114px">Get a Quote</li>
    <li style="width:101px">Our Work</li>
    <li style="width:102px">Contact us</li>
  </ul>
  <div class="call">Call us :<b>555 204 7731</b></div>
</nav>

<header class="hero">
  <div class="abs logo">
    <span class="logo-mark"></span>
    <span class="logo-name">Hollow Ridge<br>Groundcare</span>
  </div>
  <div class="abs rule" style="top:117px"></div>
  <h1 class="abs welcome">Welcome to HRG</h1>
  <p class="abs intro">Nullam ullamcorper molestie arcu eu posuere. Vestibulum ante ipsum primis in faucibus orci luctus et ultrices posuere cubilia Curae; Vestibu lum ante ipsum primis in faucibus orci luctus et ultrices posuere cubilia Curae; Ut non mauris dui. Aenean vel tristique lorem. Sed vulputate erat eu odio aliquet nec porta purus mollis.</p>
  <div class="abs quote-btn">
    <svg width="19" height="20" viewBox="0 0 19 20"><rect x="2" y="1" width="14" height="18" fill="#fff" stroke="#a85a10"/><path d="M5 6h8M5 9h8M5 12h6" stroke="#a85a10"/></svg>
    GET A QUOTE
  </div>
  <div class="abs rule" style="top:325px"></div>
  <div class="abs slider"><div class="ph" role="img" aria-label="Looking up into the pale trunks and green canopy of tall gum trees against the sky"></div></div>
  <div class="abs slider-arrows">
    <svg width="22" height="22" viewBox="0 0 22 22"><circle cx="11" cy="11" r="10" fill="#eee" stroke="#999"/><path d="M13 7l-5 4 5 4z" fill="#333"/></svg>
    <svg width="22" height="22" viewBox="0 0 22 22"><circle cx="11" cy="11" r="10" fill="#eee" stroke="#999"/><path d="M9 7l5 4-5 4z" fill="#333"/></svg>
  </div>
</header>

<section class="feature" style="left:81px">
  <h2>Tree Pruning</h2>
  <div class="frame"><div class="ph" role="img" aria-label="Climber pruning branches high in a leafy tree" style="background:linear-gradient(135deg,#2f5a22,#6f9a3e 60%,#b8d49a)"></div></div>
  <p>Sed dui lacus, consectetur eu congue in, luctus ut ante. Vivamus tincidunt tempor enim, non pretium odio molestie sed. Praesent id metus vel nunc ornare aliquam. mauris a orci erat.</p>
  <span class="btn-more">View more</span>
</section>
<section class="feature" style="left:356px">
  <h2>Stump Grinding</h2>
  <div class="frame"><div class="ph" role="img" aria-label="Stump grinder wheel cutting into a tree stump" style="background:linear-gradient(135deg,#b89a2c,#8a6a48 45%,#6b4a32)"></div></div>
  <p>Sed dui lacus, consectetur eu congue in, luctus ut ante. Vivamus tincidunt tempor enim, non pretium odio molestie sed. Praesent id metus vel nunc ornare aliquam. mauris a orci erat.</p>
  <span class="btn-more">View more</span>
</section>
<section class="feature" style="left:631px">
  <h2>Line clearing</h2>
  <div class="frame"><div class="ph" role="img" aria-label="Workers clearing tall trees against a blue sky" style="background:linear-gradient(#5a8fd8,#7eaaf0 60%,#4e6a3a)"></div></div>
  <p>Sed dui lacus, consectetur eu congue in, luctus ut ante. Vivamus tincidunt tempor enim, non pretium odio molestie sed. Praesent id metus vel nunc ornare aliquam. mauris a orci erat.</p>
  <span class="btn-more">View more</span>
</section>

<div class="abs divider"></div>

<section class="abs services">
  <h2 class="section-title">Our Services</h2>
  <ul>
    <li><svg width="20" height="20" viewBox="0 0 20 20"><circle cx="10" cy="10" r="9" fill="#e8801e"/><path d="M8 6l4 4-4 4" stroke="#fff" stroke-width="2" fill="none"/></svg>Diagnosis</li>
    <li><svg width="20" height="20" viewBox="0 0 20 20"><circle cx="10" cy="10" r="9" fill="#e8801e"/><path d="M8 6l4 4-4 4" stroke="#fff" stroke-width="2" fill="none"/></svg>Treatment</li>
    <li><svg width="20" height="20" viewBox="0 0 20 20"><circle cx="10" cy="10" r="9" fill="#e8801e"/><path d="M8 6l4 4-4 4" stroke="#fff" stroke-width="2" fill="none"/></svg>Purnign</li>
    <li><svg width="20" height="20" viewBox="0 0 20 20"><circle cx="10" cy="10" r="9" fill="#e8801e"/><path d="M8 6l4 4-4 4" stroke="#fff" stroke-width="2" fill="none"/></svg>Tree Removal</li>
    <li><svg width="20" height="20" viewBox="0 0 20 20"><circle cx="10" cy="10" r="9" fill="#e8801e"/><path d="M8 6l4 4-4 4" stroke="#fff" stroke-width="2" fill="none"/></svg>Stump Removal</li>
    <li><svg width="20" height="20" viewBox="0 0 20 20"><circle cx="10" cy="10" r="9" fill="#e8801e"/><path d="M8 6l4 4-4 4" stroke="#fff" stroke-width="2" fill="none"/></svg>Cabling &amp; Bracing</li>
    <li><svg width="20" height="20" viewBox="0 0 20 20"><circle cx="10" cy="10" r="9" fill="#e8801e"/><path d="M8 6l4 4-4 4" stroke="#fff" stroke-width="2" fill="none"/></svg>Arborist Consults</li>
    <li><svg width="20" height="20" viewBox="0 0 20 20"><circle cx="10" cy="10" r="9" fill="#e8801e"/><path d="M8 6l4 4-4 4" stroke="#fff" stroke-width="2" fill="none"/></svg>Tree Protection</li>
  </ul>
</section>

<section class="abs about">
  <h2 class="section-title">About HRG</h2>
  <p>Nullam consequat porta libero, sit amet ultricies ipsum molestie et. In felis nunc, malesuada nec ultricies eu, dictum eu tellus. Pellentesque ultrices est quis magna condimentum ultrices elementum elit convallis. Vestibulum libero est, varius quis sodales sit amet, malesuada ut sapien. Sed vel est massa. Nullam blandit nisl vel sapien consectetur tristique. Donec purus nunc, pulvinar at rutrum vitae.</p>
  <div class="mascot" role="img" aria-label="Illustration of an arborist in a hard hat beside a small tree"></div>
</section>

<div class="abs gallery">
  <div class="frame"><div class="ph" role="img" aria-label="Hand pruning green foliage with secateurs" style="background:linear-gradient(135deg,#2f5a26,#5f8f3e)"></div></div>
  <div class="frame"><div class="ph" role="img" aria-label="Large bare tree against blue sky over buildings" style="background:linear-gradient(#2f6fd0,#86aee0 60%,#6a7060)"></div></div>
  <div class="frame"><div class="ph" role="img" aria-label="Young tree with fresh spring leaves" style="background:linear-gradient(135deg,#6f8a4a,#a9bf7c)"></div></div>
</div>

<footer class="footer">
  <h3 style="left:84px;top:18px">Contact us</h3>
  <div class="abs map"><div class="ph" role="img" aria-label="Street map showing the office location"></div></div>
  <address class="abs contact">14 Fernbrook Lane<br>Ashvale, WA 6990<br>Call : 08 5550 2418<br>Fax :&nbsp; 08 5550 2419<br>Email : hello@hrg.example</address>
  <div class="vline" style="left:355px"></div>
  <h3 style="left:392px;top:18px">Testimonials</h3>
  <p class="abs testimonial"><span class="quote-mark">&ldquo;</span>&nbsp;&nbsp;&nbsp;&nbsp; Eros, gravida sed tincidunt sed, Mauris imperdiet tellus eu est interdum massa. Maecenas tincidunt imperd. &nbsp;<span class="quote-mark">&rdquo;</span></p>
  <div class="abs customer">Customer Name,City</div>
  <div class="vline" style="left:621px"></div>
  <h3 style="left:646px;top:18px">Connect with us :</h3>
  <div class="abs social"><span></span><span></span><span></span><span></span></div>
  <div class="abs copy">Copyright &copy;&nbsp; 2013 &nbsp; www.hrg.example<br>All rights reserved.</div>
</footer>

</body>
</html>
```